Business card for Real Estate Company located in Coastal area of spain

Want a business card design. Simple, professional, horizontal layout. will be 2 sided. Name of company (logo big on front). Name of agent, phone and email address. Back side will be list of general services we provide. Would like to see 2 separate concepts using the 2 separate logo treatments. One using Rich dark, bright blue as the stock color, and the other using White as the stock color.
Logo files uploaded (2 different versions) Domain (bayridgedwell48.com) Moraira-Calpe-Altea-Javea-Denia-Marina Alta Area (perhaps across the bottom of the front of card0 Petra Linde Licensed Estate Agent / Partner Petra@bayridgedwell48.com +34.681.72.40.96 Back of card should list services offered

Real Estate Sales and Investments Real Estate Rental Management Kitchen, Bathroom Reformations Complete Home Reformation Services Window and Door Replacement Landscape and Garden Management Pool and Jacuzzi Service

Target Market(s)

Real estate and construction

Industry/Entity Type

Real Estate

Contact Information for Business Card

Logo files uploaded (2 different versions) Domain (bayridgedwell48.com) Moraira-Calpe-Altea-Javea-Denia-Marina Alta Area (perhaps across the bottom of the front of card0 Petra Linde Licensed Estate Agent / Partner Petra@bayridgedwell48.com +34.681.72.40.96

Colors

Designer to choose colors to be used in the design.

Requirements
Must have
• progressive look professional
Nice to have
• Front big logo, Agent details. Back, list of services included in project description
Should not have
• Gloss finish for card

```html
<!DOCTYPE html>
<html lang="en">
<head>
<meta charset="utf-8">
<title>Bayridgedwell48 Business Card</title>
<link href="https://fonts.googleapis.com/css2?family=Montserrat:wght@400;500;700&display=swap" rel="stylesheet">
<style>
  :root{
    --backdrop:#1d1d1f;
    --stock:#3b3b3d;
    --accent:#c660c2;
    --ink:#f2f2f2;
    --ink-soft:#d8d8da;
  }
  *{margin:0;padding:0;box-sizing:border-box}
  html,body{width:1200px;height:900px;overflow:hidden}
  body{
    background:var(--backdrop);
    font-family:"Montserrat",Arial,sans-serif;
    color:var(--ink);
    display:flex;flex-direction:column;align-items:center;justify-content:center;gap:40px;
  }
  .card{
    position:relative;width:700px;height:400px;
    background:var(--stock);border-radius:18px;overflow:hidden;
    border-bottom:7px solid var(--accent);
  }
  .wordmark{font-weight:400;color:var(--ink);letter-spacing:0.3px;line-height:1;white-space:nowrap}
  .tagline{font-size:7px;font-weight:700;letter-spacing:2.4px;color:var(--ink-soft);margin-top:6px;text-transform:uppercase;white-space:nowrap}

  /* Back */
  .card-back .brand{position:absolute;left:40px;top:212px}
  .card-back .wordmark{font-size:22px}
  .card-back .divider{position:absolute;left:330px;top:78px;width:1.5px;height:170px;background:var(--accent)}
  .services{position:absolute;left:356px;top:82px;list-style:none}
  .services li{font-size:14px;line-height:24px;color:var(--ink-soft);display:flex;align-items:center;white-space:nowrap}
  .services li::before{content:"";width:5px;height:5px;border-radius:50%;background:var(--accent);margin-right:14px;flex:none}
  .license{position:absolute;left:356px;top:300px;font-size:13px;color:var(--ink-soft)}

  /* Front */
  .card-front .brand{position:absolute;left:48px;top:48px}
  .card-front .wordmark{font-size:42px}
  .card-front .tagline{font-size:9px;letter-spacing:3.4px}
  .agent{position:absolute;left:48px;top:196px}
  .agent-name{font-size:26px;font-weight:700;color:var(--accent)}
  .agent-role{font-size:14px;color:var(--ink-soft);margin-top:4px}
  .rule{position:absolute;left:48px;top:262px;width:604px;height:1.5px;background:var(--accent)}
  .area{position:absolute;right:48px;top:214px;text-align:right;font-size:13px;line-height:19px;color:var(--ink-soft)}
  .contacts{position:absolute;left:48px;top:280px;list-style:none}
  .contacts li{display:flex;align-items:center;gap:14px;font-size:14px;line-height:26px;color:var(--ink-soft)}
  .contacts svg{width:14px;height:14px;flex:none}
  .icon-fill{fill:var(--accent)}
  .icon-line{fill:none;stroke:var(--accent);stroke-width:2.4;stroke-linejoin:round}
</style>
</head>
<body>
  <section class="card card-back">
    <div class="brand">
      <div class="wordmark">Bayridgedwell48.com</div>
      <div class="tagline">Real Estate-Reforms-Home Services</div>
    </div>
    <div class="divider"></div>
    <ul class="services">
      <li>Real Estate Sales and Investments</li>
      <li>Real Estate Rental Management Kitchen</li>
      <li>Bathroom Reformations</li>
      <li>Complete Home Reformation Services</li>
      <li>Window and Door Replacement</li>
      <li>Landscape and Garden Management</li>
      <li>Pool and Jacuzzi Service</li>
    </ul>
    <div class="license">License Number 01234567</div>
  </section>

  <section class="card card-front">
    <div class="brand">
      <div class="wordmark">Bayridgedwell48.com</div>
      <div class="tagline">Real Estate-Reforms-Home Services</div>
    </div>
    <div class="agent">
      <div class="agent-name">Petra Linde</div>
      <div class="agent-role">Estate Agent / Partner</div>
    </div>
    <div class="area">Moraira-Calpe-Altea-Javea-<br>Denia-Marina Alta Area</div>
    <div class="rule"></div>
    <ul class="contacts">
      <li><svg viewBox="0 0 24 24" aria-hidden="true"><path class="icon-fill" d="M6.6 10.8a15.1 15.1 0 0 0 6.6 6.6l2.2-2.2a1 1 0 0 1 1-.25 11.4 11.4 0 0 0 3.6.57 1 1 0 0 1 1 1V20a1 1 0 0 1-1 1A17 17 0 0 1 3 4a1 1 0 0 1 1-1h3.5a1 1 0 0 1 1 1c0 1.25.2 2.45.57 3.57a1 1 0 0 1-.25 1z"/></svg>+34.681.72.40.96</li>
      <li><svg viewBox="0 0 24 24" aria-hidden="true"><path class="icon-line" d="M3 6h18v12H3z M3 6l9 7 9-7"/></svg>Petra@bayridgedwell48.com</li>
      <li><svg viewBox="0 0 24 24" aria-hidden="true"><circle class="icon-line" cx="12" cy="12" r="9"/><path class="icon-line" d="M3 12h18 M12 3c3 3 3 15 0 18 M12 3c-3 3-3 15 0 18"/></svg>www.bayridgedwell48.com</li>
    </ul>
  </section>
</body>
</html>
```